Purchasing community for life science startups needs landing page for collecting of contact adresses

We are the "Pipette Union", the first purchasing community for life science startups. The idea is to bundle the needs of several smaller companies (laboratories) and to buy lab consumables and chemicals in larger quantities. This bargaining position, at the end of all participants can buy their products very low prices. In the attached powerpoint file you will find an idea and some elements, which demonstrate a little the style, which came into my mind.
Urlaub/Ferien
Target Market(s)
Our target customers are startups and smaller biotech companies, which are too small to get the best prices. The aim of this landing page is to collect all interested parties.
Look and feel

```html
<!DOCTYPE html>
<html lang="de">
<head>
<meta charset="utf-8">
<title>Pipette Union – Einkaufsgemeinschaft LifeScience</title>
<link rel="stylesheet" href="https://fonts.googleapis.com/css2?family=Open+Sans:wght@400;600;700;800&display=swap">
<style>
:root{
  --ink:#1d5d8e;
  --ink-dark:#16415f;
  --accent:#12aeea;
  --green:#2eae4e;
  --text:#333;
  --muted:#777;
  --soft:#f6f7f8;
  --white:#fff;
}
*{box-sizing:border-box;margin:0;padding:0}
html,body{width:1200px;height:2927px;overflow:hidden;background:var(--white);font-family:"Open Sans",Arial,sans-serif;color:var(--text)}
.page{position:relative;width:1200px;height:2927px}
.abs{position:absolute}

/* hero */
.hero{left:28px;top:0;width:1144px;height:488px;background:linear-gradient(90deg,#f4f6f8 0%,#ffffff 45%,#eef3f6 100%)}
.hero-art{right:0;top:60px;width:560px;height:420px;background:radial-gradient(ellipse at 55% 60%,#8fdcf5 0%,#cfeefa 35%,#eef5f8 70%,rgba(255,255,255,0) 100%)}
.hero-side{left:0;top:160px;width:70px;height:330px;background:linear-gradient(180deg,rgba(120,200,120,.45),rgba(200,230,200,.15))}
.brand{left:80px;top:34px;display:flex;align-items:center;gap:14px}
.brand-mark{width:84px;height:84px;background:var(--ink)}
.brand-name{font-weight:700;font-size:36px;line-height:1;color:var(--ink-dark);letter-spacing:.5px}
.brand-sub{font-size:22px;color:var(--ink-dark);margin-top:4px}
.hero-title{left:110px;top:168px;font-size:48px;font-weight:700;line-height:1.18;color:var(--ink)}
.hero-sub{left:110px;top:290px;font-size:30px;line-height:1.25;color:var(--ink)}
.btn{display:flex;align-items:center;justify-content:center;background:var(--accent);color:var(--white);font-weight:600;border-radius:12px;box-shadow:0 4px 8px rgba(0,0,0,.12);z-index:2}
.btn-hero{left:104px;top:380px;width:222px;height:52px;font-size:23px}

/* questions */
.checks{left:78px;top:548px}
.check-row{display:flex;align-items:flex-start;gap:30px;margin-bottom:22px;font-size:35px;line-height:1.25;color:var(--ink)}
.check-row svg{flex:none;margin-top:6px}
.invite{left:154px;top:784px;font-size:24px;color:var(--ink)}
.btn-more{left:150px;top:838px;width:220px;height:52px;font-size:23px}

/* principles */
.principles{left:28px;top:952px;width:1144px;height:566px;background:var(--white);box-shadow:0 0 8px rgba(0,0,0,.14)}
.card{top:40px;width:258px;background:var(--white);box-shadow:0 2px 7px rgba(0,0,0,.16)}
.card-head{height:66px;background:var(--accent);color:var(--white);font-weight:700;font-size:20px;display:flex;align-items:center;justify-content:center;gap:8px}
.card-body{padding:22px 18px 26px;font-size:15.5px;line-height:1.5;color:#555}

/* benefits */
.product-art{left:58px;top:1580px;width:322px;height:330px;background:linear-gradient(150deg,#d7b083 0%,#c19566 55%,#9c7346 100%)}
.deco-art{left:960px;top:1640px;width:210px;height:270px;background:linear-gradient(180deg,rgba(220,225,230,0),rgba(220,225,230,.45))}
.benefit-title{left:396px;top:1562px;font-size:51px;font-weight:800;color:var(--ink);letter-spacing:.5px}
.benefit-lead{left:404px;top:1635px;font-size:29px;line-height:1.25;color:#333}
.benefits{left:418px;top:1744px;z-index:2}
.benefits .check-row{font-size:32px;line-height:1.2;color:#333;margin-bottom:6px;gap:20px}
.benefits .check-row svg{margin-top:4px}

/* signup */
.signup{left:28px;top:1925px;width:1144px;height:454px;background:var(--soft)}
.signup-text{left:370px;top:1958px;font-size:26px;line-height:1.6;color:#333}
.btn-start{left:362px;top:2116px;width:222px;height:52px;font-size:23px}
.feedback{left:70px;top:2232px;width:1060px;text-align:center;font-size:26.5px;line-height:1.45;color:var(--muted)}

/* form band */
.band{left:28px;top:2379px;width:1144px;height:530px;background:var(--accent)}
.form{left:300px;top:2438px;width:542px;height:304px;background:var(--white)}
.field{position:absolute;top:102px;height:26px;border:2px solid #ccc;border-radius:14px;font-size:12px;color:#999;padding:3px 10px}
.field.active{border-color:var(--accent);box-shadow:0 0 6px rgba(18,174,234,.45)}
.message{position:absolute;left:22px;top:156px;width:498px;height:72px;border:2px solid #ccc;border-radius:14px}
.submit{position:absolute;left:218px;top:250px;width:106px;height:24px;border-radius:12px;background:var(--ink);color:var(--white);font-size:9px;font-weight:700;display:flex;align-items:center;justify-content:center}
.social{left:0;top:2804px;width:1200px;display:flex;justify-content:center;gap:60px}
.social-item{display:flex;align-items:center;gap:10px;color:var(--white);font-weight:600;font-size:26px}
.social-dot{width:40px;height:40px;border-radius:50%;background:var(--white)}
</style>
</head>
<body>
<div class="page">

  <section class="abs hero">
    <div class="abs hero-side" role="img" aria-label="Unscharfe Laborglaswaren mit grüner Flüssigkeit"></div>
    <div class="abs hero-art" role="img" aria-label="Mikroskop und Erlenmeyerkolben mit blauer Flüssigkeit auf hellem Labortisch"></div>
  </section>

  <header class="abs brand">
    <div class="brand-mark"></div>
    <div>
      <div class="brand-name">PIPETTE UNION</div>
      <div class="brand-sub">Einkaufsgemeinschaft LifeScience</div>
    </div>
  </header>

  <h1 class="abs hero-title">Gemeinsam einkaufen<br>zu Großhandelspreisen</h1>
  <p class="abs hero-sub">Die erste Einkaufsgemeinschaft der<br>forschenden LifeSience StartUPs und KMU</p>
  <div class="abs btn btn-hero">Get Started Now</div>

  <section class="abs checks">
    <div class="check-row"><svg width="38" height="38" viewBox="0 0 38 38"><circle cx="19" cy="19" r="19" fill="var(--green)"/><path d="M10 19l6 6 12-12" stroke="#fff" stroke-width="4.5" fill="none"/></svg><span>Betreibst du ein LifeScience Labor?</span></div>
    <div class="check-row"><svg width="38" height="38" viewBox="0 0 38 38"><circle cx="19" cy="19" r="19" fill="var(--green)"/><path d="M10 19l6 6 12-12" stroke="#fff" stroke-width="4.5" fill="none"/></svg><span>Benötigst du regelmäßig Laborbedarf?</span></div>
    <div class="check-row"><svg width="38" height="38" viewBox="0 0 38 38"><circle cx="19" cy="19" r="19" fill="var(--green)"/><path d="M10 19l6 6 12-12" stroke="#fff" stroke-width="4.5" fill="none"/></svg><span>Möchtest du immer alle Artikel ohne<br>Verhandlungen zum besten Preis erhalten?</span></div>
  </section>
  <p class="abs invite">Dann mach mit und werde Teilnehmer der ersten Pipette Union.</p>
  <div class="abs btn btn-more">Learn More</div>

  <section class="abs principles">
    <article class="abs card" style="left:28px">
      <div class="card-head"><svg width="20" height="20" viewBox="0 0 20 20"><circle cx="10" cy="10" r="10" fill="#fff"/><path d="M5 10l3.5 3.5L15 7" stroke="var(--accent)" stroke-width="2.5" fill="none"/></svg>Unser Ziel</div>
      <div class="card-body">Aufbau der ersten Einkaufsgemeinschaft für LifeScience Labore, über die jeder Teilnehmer seinen Laborbedarf zu Großhandelspreisen decken kann.</div>
    </article>
    <article class="abs card" style="left:305px">
      <div class="card-head" style="font-size:17px"><svg width="20" height="20" viewBox="0 0 20 20"><circle cx="10" cy="10" r="10" fill="#fff"/><path d="M5 10l3.5 3.5L15 7" stroke="var(--accent)" stroke-width="2.5" fill="none"/></svg>Das Kampagnenprinzip</div>
      <div class="card-body">Wir bündeln den Jahresbedarf an Chemikalien, Verbrauchsmaterialien und Laborbedarf unserer Teilnehmer und begegnen Herstellern als gern gesehener Großabnehmer. Je mehr Teilnehmer mitmachen, desto größer unsere Verhandlungsmasse, desto besser unsere Einkaufspreise.</div>
    </article>
    <article class="abs card" style="left:580px">
      <div class="card-head"><svg width="20" height="20" viewBox="0 0 20 20"><circle cx="10" cy="10" r="10" fill="#fff"/><path d="M5 10l3.5 3.5L15 7" stroke="var(--accent)" stroke-width="2.5" fill="none"/></svg>Keep it simple</div>
      <div class="card-body">Wir verzichten auf Rahmenverträge, Mindestbestellmengen oder sonstigen Verpflichtungen! Ihr entscheidet: Gefallen euch die Preise, dann reservieren wir für euch euren Jahresbedarf und ihr kauft ganz regulär. Kauft ihr weniger ab? Kein Problem, der Einkaufsgemeinschaft entsteht hierdurch kein Schaden. Unsere Lieferanten sind absolut kundenorientiert und kulant.</div>
    </article>
    <article class="abs card" style="left:856px">
      <div class="card-head"><svg width="20" height="20" viewBox="0 0 20 20"><circle cx="10" cy="10" r="10" fill="#fff"/><path d="M5 10l3.5 3.5L15 7" stroke="var(--accent)" stroke-width="2.5" fill="none"/></svg>Fairness</div>
      <div class="card-body">Jeder Teilnehmer trägt entscheidend dazu bei, dass die Gemeinschaft optimale Preise erhält und wachsen kann. Deshalb gelten die Preise für alle, ganz unabhängig von (unverbindlich) angemeldeten Abnahmemengen.</div>
    </article>
  </section>

  <section class="abs signup"></section>

  <div class="abs deco-art" role="img" aria-label="Blasse Mikroskop-Skizze als Hintergrunddekoration"></div>
  <div class="abs product-art" role="img" aria-label="Versandkarton mit Markenaufdruck"></div>
  <h2 class="abs benefit-title">VORTEILE FÜR TEILNEHMER</h2>
  <p class="abs benefit-lead">Jeder Teilnehmer wird im Prinzip zum<br>Großabnehmer und die</p>
  <section class="abs benefits">
    <div class="check-row"><svg width="32" height="32" viewBox="0 0 38 38"><circle cx="19" cy="19" r="19" fill="var(--green)"/><path d="M10 19l6 6 12-12" stroke="#fff" stroke-width="4.5" fill="none"/></svg><span>Spare 20 - 40% im Einkauf völlig<br>ohne Verhandlungen</span></div>
    <div class="check-row"><svg width="32" height="32" viewBox="0 0 38 38"><circle cx="19" cy="19" r="19" fill="var(--green)"/><path d="M10 19l6 6 12-12" stroke="#fff" stroke-width="4.5" fill="none"/></svg><span>mehr Zeit für euer Kerngeschäft</span></div>
    <div class="check-row"><svg width="32" height="32" viewBox="0 0 38 38"><circle cx="19" cy="19" r="19" fill="var(--green)"/><path d="M10 19l6 6 12-12" stroke="#fff" stroke-width="4.5" fill="none"/></svg><span>Keine Vertragsverpflichtung</span></div>
  </section>

  <p class="abs signup-text">Hast du Interesse an einer Teilnahme?<br>Dann trage dich gerne völlig unverbindlich in unsere<br>Interessentenliste ein, sodass wir Kontakt zu dir aufnehmen</p>
  <div class="abs btn btn-start">Get Started Now</div>
  <p class="abs feedback">Um einen Eindruck von unseren Preisen zu erhalten schicken wir dir eine<br>vorläufige Preisliste zu und bitten dich um feedback. Welche Artikel interessieren<br>dich? In welchen Mengen benötigst du diese? Welche fehlen noch?</p>

  <section class="abs band"></section>
  <form class="abs form">
    <div class="field active" style="left:22px;width:150px">Email</div>
    <div class="field" style="left:200px;width:150px">First Name</div>
    <div class="field" style="left:370px;width:150px">Last Name</div>
    <div class="message"></div>
    <div class="submit">SUBMIT</div>
  </form>
  <nav class="abs social">
    <div class="social-item"><span class="social-dot"></span>Linkwerk</div>
    <div class="social-item"><span class="social-dot"></span>Kontaktnetz</div>
  </nav>

</div>
</body>
</html>
```